Fashion clothing business needs a label, swing tag and business card.

Independent womenswear label called "Tessa Morwick".
I'd like a design for a woven label to go on the clothes, a swing tag and business card design. The design should be simple, modern but timeless. Its a small business, made locally in Melbourne, Australia, produces quality garments for everyday wear using beautiful fabrics.
Updates

Target Market(s)

30+ ladies, who want quality everyday wear, who don't necessarily follow trends. They can be a bit edgy and willing to take a risk with something different.

Industry/Entity Type

Clothing

Font styles to use
Other font styles liked:
• I dont mind the typewriter font, but can it look modern? happy for you to choose.

Requirements
Should not have
• A difficult shape swing tag - as it might be more expensive for me to get printed and cut.

```html
<!DOCTYPE html>
<html lang="en">
<head>
<meta charset="utf-8">
<title>Tessa Morwick – Woven Label</title>
<link rel="stylesheet" href="https://fonts.googleapis.com/css2?family=Fira+Sans:wght@500;600&display=swap">
<style>
  :root {
    --backdrop: #e6dfcc;
    --label-white: #ffffff;
    --ink: #111111;
    --bar: #1e1a1b;
  }
  * { margin: 0; padding: 0; box-sizing: border-box; }
  html, body {
    width: 1200px;
    height: 849px;
    overflow: hidden;
    background: var(--backdrop);
  }
  .canvas {
    position: relative;
    width: 1200px;
    height: 849px;
  }
  .woven-label {
    position: absolute;
    left: 310px;
    top: 370px;
    width: 745px;
    height: 445px;
    background: var(--label-white);
    border-radius: 36px;
    overflow: hidden;
  }
  .brand-mark {
    position: absolute;
    left: 50%;
    top: 22px;
    width: 150px;
    height: 150px;
    transform: translateX(-50%);
  }
  .brand-name {
    position: absolute;
    left: 0;
    right: 0;
    top: 200px;
    text-align: center;
    font-family: "Fira Sans", sans-serif;
    font-weight: 600;
    font-size: 74px;
    line-height: 1;
    color: var(--ink);
    letter-spacing: 0.5px;
  }
  .origin-line {
    position: absolute;
    left: 0;
    right: 0;
    top: 358px;
    height: 44px;
    display: flex;
    align-items: center;
  }
  .origin-bar {
    height: 20px;
    background: var(--bar);
  }
  .origin-bar--left { width: 163px; }
  .origin-bar--right { width: 167px; margin-left: auto; }
  .origin-text {
    position: absolute;
    left: 0;
    right: 0;
    text-align: center;
    font-family: "Fira Sans", sans-serif;
    font-weight: 600;
    font-size: 36px;
    line-height: 44px;
    color: var(--ink);
  }
</style>
</head>
<body>
  <main class="canvas">
    <section class="woven-label">
      <svg class="brand-mark" viewBox="0 0 150 150" aria-hidden="true">
        <circle cx="75" cy="75" r="66" fill="none" stroke="var(--ink)" stroke-width="12"/>
      </svg>
      <h1 class="brand-name">Tessa Morwick</h1>
      <div class="origin-line">
        <span class="origin-bar origin-bar--left"></span>
        <p class="origin-text">Made in Australia</p>
        <span class="origin-bar origin-bar--right"></span>
      </div>
    </section>
  </main>
</body>
</html>
```